Bold & Power Webpage for VANTA Medical a Novel Business Solution for Clinical Labs

Informative and interactive webpage that utilizes my logo and information to draw customers into our company. The consulting company has 5 major functions.
1. Scientific Support to Clinical Sales
2. Clinical Lab Consulting
3. Develops Novel Diagnostic Test for Clinical labs
4. Process Optimization for Business
5. Physician Support for clinical results

The page should be dynamic and attractive from a marketing perspective. It should access points to upload new information in the form of publications, papers and videos. The website should have a means to be educational as well with a dynamic presentation of the information.

Target Market(s)

Medical Sales Reps
Clinical Laboratories
Medical Professionals
Scientist

Coding

Number of Pages Required

Font styles to use
Serif

Requirements
Must have
• Bold Colors, Dynamic presentation, fluid transitions, ability to request info, add PDF type information, Must professional and visually impressive
Nice to have
• Ability to upload videos, request information

```html
<!DOCTYPE html>
<html lang="en">
<head>
<meta charset="utf-8">
<title>VANTA Medical – Clinical Lab Consulting</title>
<link href="https://fonts.googleapis.com/css2?family=Cinzel:wght@400;600;700&family=Lato:wght@400;700;900&display=swap" rel="stylesheet">
<style>
:root{
  --navy:#1b4f7a;
  --blue:#2a7fb8;
  --green:#5cb531;
  --green-dark:#3f8f1f;
  --ink:#222;
  --text:#555;
  --grey-bg:#eeeff1;
  --line:#c9d3dc;
  --footer:#1f1f21;
  --footer-bar:#141416;
  --orange:#f4a21c;
  --white:#fff;
}
*{box-sizing:border-box;margin:0;padding:0}
html,body{width:1200px;height:4500px;overflow:hidden}
body{position:relative;background:var(--white);font-family:'Lato',sans-serif;color:var(--text)}
.abs{position:absolute}
.serif{font-family:'Cinzel',serif}
.section-title{position:absolute;left:0;width:1200px;text-align:center;font-family:'Cinzel',serif;font-size:40px;color:var(--ink);letter-spacing:1px;font-weight:600}
.section-title span{color:var(--navy)}
.title-mark{position:absolute;left:588px;width:24px;height:8px;border-radius:4px;background:var(--line)}

/* header */
.topbar{position:absolute;top:0;left:0;width:1200px;height:40px}
.topbar .contact{position:absolute;top:8px;font-size:16px;color:#333;display:flex;align-items:center;gap:8px}
.dl-tab{position:absolute;top:0;right:40px;width:190px;height:34px;background:var(--green);color:#fff;font-weight:900;font-size:15px;display:flex;align-items:center;justify-content:center;gap:8px;border-radius:0 0 6px 6px}
.brand{position:absolute;top:18px;left:70px;width:190px;text-align:center}
.brand .mark{width:60px;height:60px;border-radius:50%;border:6px solid var(--navy);margin:0 auto 6px}
.brand .name{font-family:'Cinzel',serif;font-weight:700;font-size:28px;color:var(--navy);line-height:32px}
.nav{position:absolute;top:92px;left:350px;display:flex;gap:34px;font-family:'Cinzel',serif;font-size:17px;color:#333}
.nav .active{color:var(--navy);border-bottom:2px solid var(--navy);padding-bottom:4px}

/* hero */
.hero{position:absolute;top:168px;left:0;width:1200px;height:552px;background:linear-gradient(100deg,#c9ccc8 0%,#e9ece9 40%,#f3f5f4 65%,#d5dcdf 100%)}
.hero-caption{position:absolute;bottom:12px;left:0;width:1200px;text-align:center;color:#fff;font-weight:900;font-size:31px;line-height:40px;text-shadow:0 2px 6px rgba(0,0,0,.45)}
.hero-arrow{position:absolute;top:250px;color:#fff;font-size:40px;opacity:.8}

/* welcome */
.intro{position:absolute;top:822px;left:90px;width:1020px;font-size:14px;line-height:22px;text-align:center;color:#444}
.pillar{position:absolute;top:940px;width:260px;text-align:center}
.pillar .icon{width:74px;height:74px;border-radius:50%;margin:0 auto 18px;display:flex;align-items:center;justify-content:center}
.pillar h3{font-size:19px;font-weight:900;color:#333;margin-bottom:10px}
.pillar p{font-size:15px;line-height:20px;color:#555}

/* consulting */
.consulting{position:absolute;top:1162px;left:0;width:1200px;height:624px;background:var(--grey-bg)}
.c-label{position:absolute;font-weight:900;font-size:19px;color:#222;line-height:24px}

/* banner */
.banner{position:absolute;top:1786px;left:0;width:1200px;height:394px;background:linear-gradient(90deg,#0f2f55 0%,#1d4f86 45%,#2f6ea5 75%,#1a406d 100%)}
.banner h2{position:absolute;left:0;width:1200px;text-align:center;color:#fff;font-family:'Cinzel',serif;font-weight:400}
.cta{position:absolute;top:242px;left:430px;width:340px;height:66px;border-radius:33px;background:var(--green);color:#fff;font-size:26px;font-weight:700;display:flex;align-items:center;padding-left:86px}
.cta .dot{position:absolute;left:6px;top:5px;width:56px;height:56px;border-radius:50%;background:#fff;border:4px solid var(--green-dark)}

/* what we do */
.w-label{position:absolute;font-weight:900;font-size:17px;color:#222;line-height:21px}

/* technology */
.tech-img{position:absolute;top:2932px;height:262px;border:5px solid var(--orange);background:linear-gradient(180deg,#ffffff 0%,#f2f2f2 100%)}
.zoom{position:absolute;width:56px;height:56px;border-radius:50%;background:var(--navy);display:flex;align-items:center;justify-content:center}
.tech h3{font-size:27px;font-weight:900;color:#222;margin-bottom:16px}
.tech ul{list-style:none}
.tech li{font-size:15px;color:#444;margin-bottom:17px;display:flex;align-items:center;gap:12px}
.tick{width:16px;height:16px;flex:none}

/* stats */
.stats{position:absolute;top:3410px;left:0;width:1200px;height:418px;background:var(--grey-bg)}
.stat{position:absolute;top:102px;width:220px;text-align:center}
.stat .ring{width:120px;height:120px;margin:0 auto 18px;position:relative}
.stat .num{font-size:30px;font-weight:700;color:#222}
.stat .lbl{font-size:21px;font-weight:700;color:var(--navy);margin-top:6px}

/* news & testimonials */
.col-title{position:absolute;top:3842px;font-family:'Cinzel',serif;font-size:38px;font-weight:600;color:#222}
.col-title span{color:var(--navy)}
.news-item{position:absolute;left:82px;width:470px;height:90px}
.news-item .thumb{position:absolute;left:0;top:0;width:112px;height:84px;background:linear-gradient(135deg,#9fb3c6,#dfe6ec)}
.news-item .body{position:absolute;left:128px;top:0;width:340px}
.news-item h4{font-size:15px;font-weight:700;color:#222}
.news-item .date{font-size:12px;color:var(--green);margin:3px 0}
.news-item p{font-size:12px;line-height:16px;color:#666}
.pager{position:absolute;top:3856px;font-size:20px;color:#aaa}

/* footer */
.footer{position:absolute;top:4162px;left:0;width:1200px;height:290px;background:var(--footer);color:#ddd}
.footer h5{font-size:15px;font-weight:900;color:#fff;letter-spacing:.5px;margin-bottom:18px}
.footer .col{position:absolute;top:50px}
.footer ul{list-style:none}
.footer li{font-size:14px;margin-bottom:8px}
.field{width:220px;height:30px;background:#333336;color:#aaa;font-size:13px;padding:7px 10px;margin-bottom:7px}
.submit{display:inline-block;width:110px;height:28px;border-radius:14px;background:var(--green);color:#fff;font-size:13px;text-align:center;line-height:28px;margin-left:24px}
.f-row{display:flex;gap:10px;font-size:14px;margin-bottom:14px;line-height:18px}
.map{width:230px;height:150px;background:linear-gradient(135deg,#cfd9c6,#e9ede3 50%,#b8cde0)}
.bottom-bar{position:absolute;top:4452px;left:0;width:1200px;height:48px;background:var(--footer-bar);color:#ccc;font-size:14px}
.social{position:absolute;top:10px;width:28px;height:28px;border-radius:50%;border:2px solid #9aa}
</style>
</head>
<body>

<!-- Header -->
<header>
  <div class="topbar">
    <div class="contact" style="left:540px">
      <svg width="16" height="16" viewBox="0 0 16 16"><path d="M3 1l3 3-2 2c1 2 3 4 5 5l2-2 3 3-2 3C6 15 1 10 1 3z" fill="#333"/></svg>
      <b>+(555) 014 2290</b>
    </div>
    <div class="contact" style="left:720px">
      <svg width="18" height="14" viewBox="0 0 18 14"><rect x="1" y="1" width="16" height="12" fill="none" stroke="#333" stroke-width="1.6"/><path d="M1 1l8 7 8-7" fill="none" stroke="#333" stroke-width="1.6"/></svg>
      info@vm-labconsult.com
    </div>
    <div class="dl-tab">
      <svg width="16" height="16" viewBox="0 0 16 16"><path d="M8 1v9M4 6l4 4 4-4M2 14h12" stroke="#fff" stroke-width="2" fill="none"/></svg>
      DOWNLOAD PDF
    </div>
  </div>
  <div class="brand">
    <div class="mark"></div>
    <div class="name">VANTA<br>MEDICAL</div>
  </div>
  <nav class="nav">
    <span class="active">HOME</span><span>ABOUT US</span><span>CONSULTING AREAS</span><span>RESOURCES</span><span>VIDEO GALLERY</span><span>CONTACT US</span>
  </nav>
</header>

<!-- Hero -->
<section class="hero" role="img" aria-label="Photo of a physician at his desk consulting with a patient">
  <div class="hero-arrow" style="left:60px">‹</div>
  <div class="hero-arrow" style="right:60px">›</div>
  <div class="hero-caption">We Have The Technical Skill And Medical Licensure To Guide<br>A Potential Client From Collection of Sample To Collection of Revenue</div>
</section>

<!-- Welcome -->
<section>
  <h1 class="section-title" style="top:742px">Welcome to <span>Vanta Medical</span></h1>
  <div class="title-mark" style="top:796px"></div>
  <p class="intro">Lorem ipsum dolor sit amet, consectetuer adipiscing elit, sed diam nonummy nibh euismod tincidunt ut laoreet dolore magna aliquam erat volutpat. Ut wisi enim ad minim veniam, quis nostrud exerci tation ullamcorper suscipit lobortis nisl ut aliquip ex ea commodo consequat. Duis autem vel eum iriure dolor in hendrerit in vulputate velit esse molestie consequat, vel illum dolore eu feugiat nulla facilisis at vero eros et accumsan et iusto odio dignissim qui blandit.</p>
  <div class="pillar" style="left:185px">
    <div class="icon" style="background:var(--green)"><svg width="34" height="34" viewBox="0 0 34 34"><path d="M6 15h6v15H6zM14 15l6-11c3 0 3 3 2 7h8c2 0 3 2 2 4l-3 12c-1 2-2 3-4 3H14z" fill="#fff"/></svg></div>
    <h3>Who We Are</h3>
    <p>Lorem ipsum dolor sit amet, sed diam nonummy nibh euismod tincidunt ut laoreet dolore.</p>
  </div>
  <div class="pillar" style="left:470px">
    <div class="icon" style="background:var(--navy)"><svg width="36" height="36" viewBox="0 0 36 36"><circle cx="18" cy="9" r="5" fill="#fff"/><circle cx="8" cy="13" r="4" fill="#fff"/><circle cx="28" cy="13" r="4" fill="#fff"/><path d="M10 30c0-8 16-8 16 0zM1 28c0-6 9-7 10-4M35 28c0-6-9-7-10-4" fill="#fff"/></svg></div>
    <h3>Our Mission</h3>
    <p>Lorem ipsum dolor sit amet, sed diam nonummy nibh euismod tincidunt ut laoreet dolore.</p>
  </div>
  <div class="pillar" style="left:755px">
    <div class="icon" style="background:var(--green)"><svg width="36" height="36" viewBox="0 0 36 36"><circle cx="18" cy="18" r="14" fill="none" stroke="#fff" stroke-width="3"/><circle cx="18" cy="18" r="8" fill="none" stroke="#fff" stroke-width="3"/><circle cx="18" cy="18" r="3" fill="#fff"/></svg></div>
    <h3>Our Vision</h3>
    <p>Lorem ipsum dolor sit amet, sed diam nonummy nibh euismod tincidunt ut laoreet dolore.</p>
  </div>
</section>

<!-- Consulting areas -->
<section class="consulting">
  <h2 class="section-title" style="top:38px">Our <span>Consulting Areas</span></h2>
  <div class="title-mark" style="top:92px"></div>
  <svg class="abs" style="left:0;top:0" width="1200" height="624" viewBox="0 0 1200 624">
    <g stroke="#8aa3b8" stroke-width="2" fill="none">
      <line x1="600" y1="478" x2="600" y2="218"/>
      <line x1="600" y1="478" x2="380" y2="298"/>
      <line x1="600" y1="478" x2="820" y2="298"/>
      <line x1="600" y1="478" x2="310" y2="468"/>
      <line x1="600" y1="478" x2="890" y2="468"/>
    </g>
    <circle cx="600" cy="478" r="150" fill="#fff" stroke="#d8dee4" stroke-width="3"/>
    <circle cx="600" cy="478" r="136" fill="#fff" stroke="#1b4f7a" stroke-width="2" opacity=".35"/>
    <circle cx="600" cy="420" r="22" fill="#1b4f7a"/>
    <text x="600" y="498" text-anchor="middle" font-family="Cinzel,serif" font-weight="700" font-size="44" fill="#1b4f7a">VANTA</text>
    <text x="600" y="546" text-anchor="middle" font-family="Cinzel,serif" font-weight="700" font-size="44" fill="#1b4f7a">MEDICAL</text>
    <g>
      <circle cx="600" cy="218" r="42" fill="#fff" stroke="#5cb531" stroke-width="5"/>
      <path d="M592 200h16M595 200v14l-10 18h30l-10-18v-14" fill="none" stroke="#1b4f7a" stroke-width="3"/>
      <circle cx="380" cy="298" r="42" fill="#fff" stroke="#5cb531" stroke-width="5"/>
      <path d="M366 308h28M372 308l8-26 8 26M376 290l10-8" fill="none" stroke="#1b4f7a" stroke-width="3"/>
      <circle cx="820" cy="298" r="42" fill="#fff" stroke="#5cb531" stroke-width="5"/>
      <circle cx="820" cy="298" r="11" fill="none" stroke="#1b4f7a" stroke-width="5" stroke-dasharray="4 3"/>
      <circle cx="310" cy="468" r="42" fill="#fff" stroke="#5cb531" stroke-width="5"/>
      <circle cx="306" cy="464" r="10" fill="none" stroke="#1b4f7a" stroke-width="3"/>
      <line x1="313" y1="471" x2="324" y2="482" stroke="#1b4f7a" stroke-width="4"/>
      <circle cx="890" cy="468" r="42" fill="#fff" stroke="#5cb531" stroke-width="5"/>
      <rect x="878" y="450" width="24" height="34" rx="2" fill="none" stroke="#1b4f7a" stroke-width="3"/>
      <path d="M884 462h12M890 456v12M884 476h12" stroke="#1b4f7a" stroke-width="2.5"/>
    </g>
  </svg>
  <div class="c-label" style="top:120px;left:0;width:1200px;text-align:center">Develops Novel Diagnostic Test for Clinical labs</div>
  <div class="c-label" style="top:272px;left:140px;width:190px">Clinical Lab<br>Consulting</div>
  <div class="c-label" style="top:272px;left:872px;width:230px">Process Optimization<br>for Business</div>
  <div class="c-label" style="top:442px;left:60px;width:200px;text-align:right">Scientific Support<br>to Clinical Sales</div>
  <div class="c-label" style="top:442px;left:945px;width:200px">Physician Support<br>for clinical results</div>
</section>

<!-- Banner -->
<section class="banner" role="img" aria-label="Blue medical imagery with a stethoscope and laboratory test tubes">
  <h2 style="top:122px;font-size:35px">The Brighter Path Through Innovative Testing</h2>
  <h2 style="top:172px;font-size:40px">Vanta Medical</h2>
  <div class="cta"><span class="dot"></span>Get Started With Us</div>
</section>

<!-- What we do -->
<section>
  <h2 class="section-title" style="top:2212px">What We Do <span>For You</span></h2>
  <div class="title-mark" style="top:2266px"></div>
  <svg class="abs" style="left:0;top:2280px" width="1200" height="520" viewBox="0 0 1200 520">
    <defs>
      <radialGradient id="hub" cx="50%" cy="80%" r="60%">
        <stop offset="0" stop-color="#e3e6ea"/><stop offset="1" stop-color="#ffffff"/>
      </radialGradient>
    </defs>
    <rect x="0" y="0" width="1200" height="520" fill="url(#hub)"/>
    <circle cx="600" cy="480" r="330" fill="none" stroke="#dde2e7" stroke-width="2"/>
    <circle cx="600" cy="480" r="220" fill="#eef0f3" stroke="#dde2e7" stroke-width="2"/>
    <circle cx="600" cy="430" r="90" fill="#fff" stroke="#c9d3dc" stroke-width="3"/>
    <g fill="#fff" stroke="#cfd6dd" stroke-width="4">
      <circle cx="600" cy="112" r="40"/><circle cx="468" cy="145" r="40"/><circle cx="732" cy="145" r="40"/>
      <circle cx="376" cy="225" r="40"/><circle cx="826" cy="225" r="40"/>
      <circle cx="300" cy="340" r="40"/><circle cx="900" cy="340" r="40"/>
      <circle cx="280" cy="480" r="40"/><circle cx="918" cy="480" r="40"/>
    </g>
    <g fill="none" stroke="#2a7fb8" stroke-width="3">
      <rect x="586" y="100" width="28" height="22" rx="2"/><path d="M592 116v-6M600 116v-10M608 116v-4"/>
      <path d="M462 130v16l-8 12h28l-8-12v-16"/>
      <path d="M722 160l22-22M738 134l8 8M722 160h-4v-4"/>
      <rect x="362" y="212" width="28" height="24"/><path d="M368 222h16M368 229h10"/>
      <path d="M818 212v10l-8 16h32l-8-16v-10"/>
      <circle cx="300" cy="340" r="14"/><path d="M300 330v10l8 4"/>
      <circle cx="900" cy="340" r="12"/><path d="M893 340l5 5 9-9"/>
      <rect x="268" y="464" width="22" height="30" rx="2"/><path d="M273 478l4 4 8-8"/>
      <path d="M906 492l24-24M922 462l14 14"/>
    </g>
  </svg>
  <div class="w-label" style="top:2328px;left:540px;width:120px;text-align:center">GAP Analysis</div>
  <div class="w-label" style="top:2352px;left:250px;width:180px;text-align:right">ICP-MS, GC-MS, GC<br>Method Development<br>For Industry</div>
  <div class="w-label" style="top:2386px;left:778px;width:140px">Regulatory<br>Review</div>
  <div class="w-label" style="top:2478px;left:220px;width:110px;text-align:right">Project<br>Planning</div>
  <div class="w-label" style="top:2478px;left:874px;width:200px">Endogenous Biomarker<br>Quantification</div>
  <div class="w-label" style="top:2598px;left:130px;width:120px;text-align:right">Process<br>Optimization</div>
  <div class="w-label" style="top:2598px;left:950px;width:170px">Quality Management<br>System</div>
  <div class="w-label" style="top:2708px;left:70px;width:160px;text-align:right">Clinical Method<br>Development<br>&amp; Validation</div>
  <div class="w-label" style="top:2738px;left:968px;width:120px">Laboratory<br>Setup</div>
</section>

<!-- Technology -->
<section>
  <h2 class="section-title" style="top:2838px">Our <span>Technology</span></h2>
  <div class="title-mark" style="top:2892px"></div>
  <div class="tech-img" style="left:108px;width:425px" role="img" aria-label="Metabolic pathway diagram with molecular structures"></div>
  <div class="zoom" style="left:505px;top:3168px"><svg width="24" height="24" viewBox="0 0 24 24"><circle cx="10" cy="10" r="7" fill="none" stroke="#fff" stroke-width="3"/><line x1="15" y1="15" x2="22" y2="22" stroke="#fff" stroke-width="3"/></svg></div>
  <div class="tech-img" style="left:650px;width:430px" role="img" aria-label="Steroid biosynthesis pathway chart"></div>
  <div class="zoom" style="left:1052px;top:3068px"><svg width="24" height="24" viewBox="0 0 24 24"><circle cx="10" cy="10" r="7" fill="none" stroke="#fff" stroke-width="3"/><line x1="15" y1="15" x2="22" y2="22" stroke="#fff" stroke-width="3"/></svg></div>
  <div class="tech abs" style="left:130px;top:3198px;width:430px">
    <h3>Lorem ipsum dolor sit amet</h3>
    <ul>
      <li><svg class="tick" viewBox="0 0 16 16"><rect x="1" y="1" width="14" height="14" fill="none" stroke="#2a7fb8" stroke-width="1.5"/><path d="M4 8l3 3 6-7" fill="none" stroke="#2a7fb8" stroke-width="2"/></svg>Quis Nostrud Exerci Tation Ullamcorper</li>
      <li><svg class="tick" viewBox="0 0 16 16"><rect x="1" y="1" width="14" height="14" fill="none" stroke="#2a7fb8" stroke-width="1.5"/><path d="M4 8l3 3 6-7" fill="none" stroke="#2a7fb8" stroke-width="2"/></svg>Duis autem vel eum iriure dolor in hendrerit in vulputate</li>
      <li><svg class="tick" viewBox="0 0 16 16"><rect x="1" y="1" width="14" height="14" fill="none" stroke="#2a7fb8" stroke-width="1.5"/><path d="M4 8l3 3 6-7" fill="none" stroke="#2a7fb8" stroke-width="2"/></svg>vel illum dolore eu feugiat nulla facilisis</li>
      <li><svg class="tick" viewBox="0 0 16 16"><rect x="1" y="1" width="14" height="14" fill="none" stroke="#2a7fb8" stroke-width="1.5"/><path d="M4 8l3 3 6-7" fill="none" stroke="#2a7fb8" stroke-width="2"/></svg>luptatum zzril delenit augue duis dolore</li>
    </ul>
  </div>
  <div class="tech abs" style="left:670px;top:3198px;width:430px">
    <h3>Lorem ipsum dolor sit amet</h3>
    <ul>
      <li><svg class="tick" viewBox="0 0 16 16"><rect x="1" y="1" width="14" height="14" fill="none" stroke="#2a7fb8" stroke-width="1.5"/><path d="M4 8l3 3 6-7" fill="none" stroke="#2a7fb8" stroke-width="2"/></svg>Quis Nostrud Exerci Tation Ullamcorper</li>
      <li><svg class="tick" viewBox="0 0 16 16"><rect x="1" y="1" width="14" height="14" fill="none" stroke="#2a7fb8" stroke-width="1.5"/><path d="M4 8l3 3 6-7" fill="none" stroke="#2a7fb8" stroke-width="2"/></svg>Duis autem vel eum iriure dolor in hendrerit in vulputate</li>
      <li><svg class="tick" viewBox="0 0 16 16"><rect x="1" y="1" width="14" height="14" fill="none" stroke="#2a7fb8" stroke-width="1.5"/><path d="M4 8l3 3 6-7" fill="none" stroke="#2a7fb8" stroke-width="2"/></svg>vel illum dolore eu feugiat nulla facilisis</li>
      <li><svg class="tick" viewBox="0 0 16 16"><rect x="1" y="1" width="14" height="14" fill="none" stroke="#2a7fb8" stroke-width="1.5"/><path d="M4 8l3 3 6-7" fill="none" stroke="#2a7fb8" stroke-width="2"/></svg>luptatum zzril delenit augue duis dolore</li>
    </ul>
  </div>
</section>

<!-- Sales & Support -->
<section class="stats">
  <h2 class="section-title" style="top:40px">Sales &amp; <span>Support</span></h2>
  <div class="title-mark" style="top:94px"></div>
  <div class="stat" style="left:235px">
    <svg class="ring" viewBox="0 0 120 120"><path d="M20 85A46 46 0 0 1 60 14" fill="none" stroke="#2a7fb8" stroke-width="7"/><path d="M100 35A46 46 0 0 1 60 106" fill="none" stroke="#5cb531" stroke-width="7"/><circle cx="60" cy="60" r="34" fill="#fff"/><path d="M54 40h12M57 40v16l-10 18h26l-10-18v-16" fill="none" stroke="#1b4f7a" stroke-width="4"/></svg>
    <div class="num">1500</div><div class="lbl">Lab</div>
  </div>
  <div class="stat" style="left:490px">
    <svg class="ring" viewBox="0 0 120 120"><path d="M20 85A46 46 0 0 1 60 14" fill="none" stroke="#2a7fb8" stroke-width="7"/><path d="M100 35A46 46 0 0 1 60 106" fill="none" stroke="#5cb531" stroke-width="7"/><circle cx="60" cy="60" r="34" fill="#fff"/><rect x="48" y="40" width="8" height="36" rx="4" fill="none" stroke="#1b4f7a" stroke-width="4"/><rect x="64" y="40" width="8" height="36" rx="4" fill="none" stroke="#1b4f7a" stroke-width="4"/></svg>
    <div class="num">900</div><div class="lbl">Samples Analysed</div>
  </div>
  <div class="stat" style="left:745px">
    <svg class="ring" viewBox="0 0 120 120"><path d="M20 85A46 46 0 0 1 60 14" fill="none" stroke="#2a7fb8" stroke-width="7"/><path d="M100 35A46 46 0 0 1 60 106" fill="none" stroke="#5cb531" stroke-width="7"/><circle cx="60" cy="60" r="34" fill="#fff"/><circle cx="60" cy="50" r="10" fill="#1b4f7a"/><path d="M40 82c0-16 40-16 40 0z" fill="#1b4f7a"/></svg>
    <div class="num">2000</div><div class="lbl">Satisfied Doctor</div>
  </div>
</section>

<!-- News & testimonials -->
<section>
  <h2 class="col-title" style="left:82px">Latest <span>News</span></h2>
  <div class="pager" style="left:515px">‹ ›</div>
  <div class="abs" style="left:82px;top:3898px;width:470px;height:2px;background:#e3e3e3"></div>
  <article class="news-item" style="top:3912px">
    <div class="thumb" role="img" aria-label="Hand writing a prescription"></div>
    <div class="body"><h4>ipsum dolor sit amet, sed diam nonummy</h4><div class="date">Posted on August 2, 2016</div><p>Duis autem vel eum iriure dolor in hendrerit in vulputate velit esse molestie consequat. Lorem... »</p></div>
  </article>
  <article class="news-item" style="top:4020px">
    <div class="thumb" role="img" aria-label="Doctor typing on a laptop"></div>
    <div class="body"><h4>ipsum dolor sit amet, sed diam nonummy</h4><div class="date">Posted on May 31, 2016</div><p>Duis autem vel eum iriure dolor in hendrerit in vulputate velit esse molestie consequat. Lorem... »</p></div>
  </article>

  <h2 class="col-title" style="left:620px">Client <span>Testimonials</span></h2>
  <div class="pager" style="left:1085px">‹ ›</div>
  <div class="abs" style="left:620px;top:3898px;width:500px;height:2px;background:#e3e3e3"></div>
  <div class="abs serif" style="left:630px;top:3905px;font-size:60px;color:#c9d3dc">“</div>
  <p class="abs" style="left:680px;top:3918px;width:430px;font-size:13px;line-height:20px;color:#555;font-style:italic">Lorem ipsum dolor sit amet, sed diam nonummy nibh euismod tincidunt ut laoreet dolore. Lorem ipsum dolor sit amet, sed diam nonummy nibh euismod tincidunt ut laoreet dolore magna aliquam erat volutpat. Lorem ipsum dolor sit amet, sed diam nonummy nibh euismod tincidunt ut laoreet dolore.</p>
  <div class="abs" role="img" aria-label="Client portrait" style="left:618px;top:4012px;width:118px;height:118px;border-radius:50%;border:5px solid var(--blue);background:linear-gradient(135deg,#c8b8a6,#eae2d8)"></div>
  <div class="abs" style="left:706px;top:4090px;width:32px;height:32px;border-radius:50%;background:var(--green)"></div>
  <div class="abs" style="left:760px;top:4046px;font-size:24px;color:var(--green-dark)">Daniel Brooks</div>
  <div class="abs" style="left:760px;top:4084px;font-size:15px;color:#666">Customer</div>
</section>

<!-- Footer -->
<footer class="footer">
  <div class="col" style="left:82px">
    <h5>QUICK LINKS</h5>
    <ul><li>› Home</li><li>› About Us</li><li>› Consulting Areas</li><li>› Resources</li><li>› Video Gallery</li><li>› Contact Us</li></ul>
  </div>
  <div class="col" style="left:292px">
    <h5>REQUEST MORE INFORMATION</h5>
    <div class="field">Name</div><div class="field">Email</div><div class="field" style="height:44px">Message</div>
    <div style="margin-top:10px"><span class="submit">Submit</span></div>
  </div>
  <div class="col" style="left:592px">
    <h5>CONTACT DETAILS</h5>
    <div class="f-row"><svg width="14" height="18" viewBox="0 0 14 18"><path d="M7 17C2 10 1 8 1 6a6 6 0 0 1 12 0c0 2-1 4-6 11z" fill="#5cb531"/><circle cx="7" cy="6" r="2" fill="#1f1f21"/></svg><div><b>VANTA Medical</b><br>240 Lorem Ipsum Avenue<br>Suite 18, Dolor City</div></div>
    <div class="f-row"><svg width="14" height="14" viewBox="0 0 16 16"><path d="M3 1l3 3-2 2c1 2 3 4 5 5l2-2 3 3-2 3C6 15 1 10 1 3z" fill="#5cb531"/></svg>+(555) 014 2290</div>
    <div class="f-row"><svg width="14" height="14" viewBox="0 0 16 16"><path d="M3 1l3 3-2 2c1 2 3 4 5 5l2-2 3 3-2 3C6 15 1 10 1 3z" fill="#5cb531"/></svg>+(555) 014 2290</div>
    <div class="f-row"><svg width="16" height="12" viewBox="0 0 18 14"><rect x="1" y="1" width="16" height="12" fill="none" stroke="#5cb531" stroke-width="1.6"/><path d="M1 1l8 7 8-7" fill="none" stroke="#5cb531" stroke-width="1.6"/></svg>info@vm-labconsult.com</div>
  </div>
  <div class="col" style="left:882px">
    <h5>LOCATION MAP</h5>
    <div class="map" role="img" aria-label="Street map showing the office location"></div>
  </div>
</footer>
<div class="bottom-bar">
  <div class="abs" style="left:82px;top:15px">Copyright © 2016 VANTA Medical. All Rights Reserved.</div>
  <span class="social" style="left:952px"></span>
  <span class="social" style="left:992px"></span>
  <span class="social" style="left:1032px"></span>
  <span class="social" style="left:1072px"></span>
</div>

</body>
</html>
```